High quality childcare centre needs a roadside banner

We need a banner designed that advertises our achievement of being rated Exceeding Civic Nurture Benchmark. Which is the highest rating you can be award as part of the assessment and rating process.

Attached pdf is purely an example although the text as it stands needs to be incorporated.

Please see below for the corporate colors:

Magenta
C-0 M-100 Y-33 K-10
bf00bf

Green
C-78 M-0 Y-100 K-0
00bf00

Target Market(s)

Parents of young children that need childcare

Industry/Entity Type

Childcare

Font styles to use
Sans Serif

Requirements
Must have
• As it is a roadside banner the text should be big, bold and easy to read therefore do not use serif fonts
• Please change found to find
• Logo - see attached
• Supplied wording - see attached
• The specs for the banner are 4m x 1.25m or 4000mm x 1250mm
• The files need to be in the following format:
• jpg, eps and ai.
• Bleeds if relevant
Nice to have
• Other marketing road signs incorporate the attached 'grobold' font
• We also have a motto - 'out of little things, big things grow'
Should not have
• Serif fonts

```html
<!DOCTYPE html>
<html lang="en">
<head>
<meta charset="utf-8">
<title>Tiny Sprouts – Roadside Banner</title>
<link rel="stylesheet" href="https://fonts.googleapis.com/css2?family=Comic+Neue:wght@700&family=Fredoka:wght@700&display=swap">
<style>
  :root {
    --magenta: #a73b8e;
    --green: #33a83c;
    --ink: #000000;
    --paper: #ffffff;
    --badge-warm: #f2a33a;
    --badge-cool: #3aa0d8;
    --badge-red: #d8344a;
    --mascot: #a73b8e;
    --mascot-light: #c86bb3;
  }
  html, body {
    margin: 0;
    padding: 0;
    width: 1200px;
    height: 375px;
    overflow: hidden;
    background: var(--paper);
  }
  .banner {
    position: relative;
    width: 1200px;
    height: 375px;
    background: var(--paper);
    overflow: hidden;
  }
  .headline-intro {
    position: absolute;
    left: 28px;
    top: 4px;
    margin: 0;
    font-family: "Comic Neue", "Comic Sans MS", sans-serif;
    font-weight: 700;
    font-size: 88px;
    line-height: 1;
    color: var(--ink);
    white-space: nowrap;
  }
  .brand-name {
    position: absolute;
    left: 820px;
    top: 22px;
    width: 370px;
    margin: 0;
    text-align: center;
    font-family: "Comic Neue", "Comic Sans MS", sans-serif;
    font-weight: 700;
    font-size: 50px;
    line-height: 1;
    color: var(--magenta);
    white-space: nowrap;
  }
  .rule-top {
    position: absolute;
    left: 0;
    top: 94px;
    width: 880px;
    height: 7px;
    background: linear-gradient(to right, var(--magenta) 0%, var(--magenta) 55%, rgba(167,59,142,0) 100%);
  }
  .rating-badge {
    position: absolute;
    left: 26px;
    top: 118px;
    width: 168px;
    height: 150px;
  }
  .rating-title {
    position: absolute;
    left: 200px;
    top: 112px;
    width: 790px;
    margin: 0;
    text-align: center;
    font-family: "Fredoka", "Arial Rounded MT Bold", sans-serif;
    font-weight: 700;
    font-size: 70px;
    line-height: 70px;
    color: var(--ink);
    letter-spacing: 1px;
    white-space: nowrap;
  }
  .rating-title span {
    display: block;
  }
  .mascot {
    position: absolute;
    left: 1010px;
    top: 104px;
    width: 168px;
    height: 166px;
    border-radius: 40% 45% 18% 22%;
    background: linear-gradient(160deg, var(--mascot-light), var(--mascot));
  }
  .rule-green {
    position: absolute;
    left: 0;
    top: 282px;
    width: 1200px;
    height: 7px;
    background: var(--green);
  }
  .cta-band {
    position: absolute;
    left: 0;
    top: 290px;
    width: 1200px;
    height: 85px;
    background: var(--magenta);
  }
  .cta-text {
    position: absolute;
    left: 130px;
    top: 6px;
    margin: 0;
    font-family: "Comic Neue", "Comic Sans MS", sans-serif;
    font-weight: 700;
    font-size: 74px;
    line-height: 1;
    color: var(--paper);
    letter-spacing: 1px;
    white-space: nowrap;
  }
</style>
</head>
<body>
  <main class="banner">
    <h2 class="headline-intro">This service is rated</h2>
    <p class="brand-name">Tiny Sprouts</p>
    <div class="rule-top"></div>

    <svg class="rating-badge" viewBox="0 0 168 150" role="img" aria-label="Rating authority badge">
      <defs>
        <linearGradient id="badgeFill" x1="0" y1="0" x2="0" y2="1">
          <stop offset="0" stop-color="#f2a33a"/>
          <stop offset="0.5" stop-color="#3aa0d8"/>
          <stop offset="1" stop-color="#d8344a"/>
        </linearGradient>
      </defs>
      <rect x="14" y="10" width="140" height="130" rx="28" fill="url(#badgeFill)"/>
    </svg>

    <h1 class="rating-title"><span>Exceeding Civic</span><span>Nurture Benchmark</span></h1>

    <div class="mascot" role="img" aria-label="Cartoon mascot character reading a book"></div>

    <div class="rule-green"></div>
    <section class="cta-band">
      <p class="cta-text">Come in and find out why ...</p>
    </section>
  </main>
</body>
</html>
```